6X6 Modern and Professional Postcard for home furnishing company

We are a modern furniture company that is introducing a new product line. It is a new dining collection. We are sending out a 6x6 Postcard to all of our clients introducing the new line. We need to create a 6x6 postcard that is creative, professional, clean, visually attractive and very modern. We are open to possibly using a tagline although we have not thought of one yet. I have attached the template for the postcard and our product images that we are considering to use on the postcard. The following text is the only text that will be on the postcard:1) "Presenting the 2019 Q-Lorvat Dining Collection"2) the tagline, if it works and if we decide to use it3) our website, bmodern.com4) our Instagram, @qlorvatsd

Industry/Entity Type

Home Furnishing

Font styles to use
Sans Serif

Requirements
Must have
• Modern, clean, visually appealing and professional look
Nice to have
• Tagline

```html
<!DOCTYPE html>
<html lang="en">
<head>
<meta charset="utf-8">
<title>Q-Lorvat Dining Collection Postcard</title>
<link rel="stylesheet" href="https://fonts.googleapis.com/css2?family=Jost:wght@400&family=Open+Sans:wght@700&display=swap">
<style>
  :root {
    --backdrop: #e9e9e9;
    --brand-red: #d40f38;
    --deep-red: #a3132c;
    --ink: #000000;
    --band: #1b1d21;
    --concrete: #6d6c68;
    --concrete-light: #8a8883;
    --table-white: #e4e4e4;
    --paper: #ffffff;
  }
  * { margin: 0; padding: 0; box-sizing: border-box; }
  html, body {
    width: 1200px; height: 1114px; overflow: hidden;
    background: var(--backdrop);
  }
  .postcard {
    position: absolute; left: 100px; top: 57px;
    width: 1000px; height: 1000px; overflow: hidden;
    background: var(--ink);
  }
  .postcard__floor {
    position: absolute; left: 0; top: 470px; width: 1000px; height: 530px;
    background: linear-gradient(180deg, var(--ink) 0%, #1c1c1b 16%, var(--concrete) 42%, var(--concrete-light) 62%, #4a4947 84%, #0e0e0e 100%);
  }
  .postcard__product-photo {
    position: absolute; left: 70px; top: 520px; width: 860px; height: 360px;
    border-radius: 6px;
    background:
      radial-gradient(ellipse 22% 30% at 20% 35%, rgba(228,228,228,0.75), rgba(228,228,228,0) 100%),
      radial-gradient(ellipse 30% 32% at 52% 55%, rgba(228,228,228,0.8), rgba(228,228,228,0) 100%),
      radial-gradient(ellipse 20% 30% at 84% 52%, rgba(228,228,228,0.75), rgba(228,228,228,0) 100%),
      linear-gradient(180deg, #2a2a29 0%, #5e5d59 40%, #7c7a75 100%);
    box-shadow: 0 0 40px 20px rgba(0,0,0,0.25);
  }
  .postcard__shapes { position: absolute; inset: 0; pointer-events: none; }
  .headline {
    position: absolute; left: 330px; top: 95px; width: 480px;
    font-family: "Jost", sans-serif; font-weight: 400;
    color: var(--paper); text-align: center; text-transform: uppercase;
    line-height: 1;
  }
  .headline__intro { display: block; font-size: 54px; letter-spacing: 1px; }
  .headline__year { display: block; font-size: 74px; margin-top: 6px; }
  .headline__brand { display: block; font-size: 64px; margin-top: 4px; }
  .headline__line { display: block; font-size: 30px; margin-top: 16px; letter-spacing: 0.5px; }
  .contact {
    position: absolute;
    font-family: "Open Sans", sans-serif; font-weight: 700;
    font-size: 27px; color: var(--paper); white-space: nowrap;
  }
  .contact--web { left: 140px; top: 905px; }
  .contact--social { left: 520px; top: 935px; }
</style>
</head>
<body>
  <main class="postcard">
    <div class="postcard__floor"></div>
    <div class="postcard__product-photo" role="img" aria-label="Product photo: three white dining tables with angular white bases standing on a grey concrete floor"></div>
    <svg class="postcard__shapes" viewBox="0 0 1000 1000" aria-hidden="true">
      <path d="M0,220 Q520,520 1000,360 V470 H0 Z" fill="var(--ink)"/>
      <path d="M0,190 Q520,490 1000,330 V372 Q520,535 0,230 Z" fill="var(--band)"/>
      <path d="M0,0 H1000 V330 Q520,490 0,190 Z" fill="var(--brand-red)"/>
      <polygon points="95,140 185,235 40,265" fill="#23252a"/>
      <polygon points="95,140 120,222 40,265" fill="#111215"/>
      <polygon points="95,140 185,235 120,222" fill="#2f3238"/>
      <polygon points="840,485 975,455 935,560" fill="var(--brand-red)"/>
      <polygon points="840,485 920,500 935,560" fill="var(--deep-red)"/>
    </svg>
    <h1 class="headline">
      <span class="headline__intro">Presenting</span>
      <span class="headline__year">The 2019</span>
      <span class="headline__brand">Q-Lorvat</span>
      <span class="headline__line">Dining Collection</span>
    </h1>
    <p class="contact contact--web">www.qlorvat.example</p>
    <p class="contact contact--social">Instagram: @qlorvatsd</p>
  </main>
</body>
</html>
```